Webdesign project for healthcare IT company

Home, About, Solution, Contact, and Employment pages.

Please match the designs uploaded for colors and effect.

Please choose appropriate healthcare IT related photos to the content. Be sure to include the content that i've attached in the word document.

Please use the following URLs as reference:

www.veltrocare.example
www.dusk.example
www.plainagree.example

Target Market(s)

healthcare providers, doctors, nurses, c-level executives

Industry/Entity Type

Healthcare

Coding

Coded - Design and coding required

Number of Pages Required

5+ page

Font styles to use
Serif
Sans Serif

Colors
6b449b
0455a3
ffffff
333333
959595

Requirements
Must have
• B2B feel, matches the colors in the uploaded design files, images that can be purchased later that meet the content that I've uploaded

```html
<!DOCTYPE html>
<html lang="en">
<head>
<meta charset="utf-8">
<title>Rouse Technologies</title>
<link href="https://fonts.googleapis.com/css2?family=Poppins:wght@300;400;500;600&family=Rubik:wght@500&display=swap" rel="stylesheet">
<style>
:root{
  --purple:#6b449b;
  --blue:#0455a3;
  --white:#ffffff;
  --ink:#333333;
  --grey:#959595;
  --footer:#111111;
}
*{margin:0;padding:0;box-sizing:border-box}
html,body{width:860px;height:1200px;overflow:hidden}
body{font-family:"Poppins",sans-serif;color:var(--ink);background:var(--white);position:relative}
.topline{position:absolute;top:0;left:0;width:860px;height:3px;background:linear-gradient(90deg,var(--blue),var(--purple));z-index:2}
.header{position:absolute;top:0;left:0;width:860px;height:66px;background:var(--white)}
.brand{position:absolute;left:116px;top:19px;display:flex;align-items:center;gap:9px}
.brand-mark{width:26px;height:26px;background:var(--blue);border-radius:50%}
.brand-name{font-size:17px;font-weight:600;color:var(--ink);letter-spacing:1.5px}
.nav a{position:absolute;top:3px;height:63px;line-height:70px;font-size:8.8px;font-weight:500;color:#111;text-decoration:none}
.nav a.active{background:var(--blue);color:var(--white);width:51px;text-align:center}
.hero{position:absolute;top:66px;left:0;width:860px;height:374px;overflow:hidden}
.hero-photo{position:absolute;inset:0;background:
  radial-gradient(ellipse 120px 150px at 90px 140px,rgba(196,140,112,.55),transparent 70%),
  radial-gradient(ellipse 120px 150px at 770px 150px,rgba(196,140,112,.55),transparent 70%),
  radial-gradient(circle 60px at 410px 110px,rgba(40,80,170,.75),transparent 75%),
  radial-gradient(circle 45px at 300px 60px,rgba(40,80,170,.7),transparent 75%),
  radial-gradient(circle 40px at 590px 130px,rgba(40,80,170,.7),transparent 75%),
  radial-gradient(circle 35px at 700px 110px,rgba(40,80,170,.65),transparent 75%),
  radial-gradient(circle 35px at 180px 200px,rgba(40,80,170,.6),transparent 75%),
  linear-gradient(180deg,#5c6c88 0%,#56657f 55%,#6f7682 100%)}
.hero-title{position:absolute;top:194px;width:860px;text-align:center;color:var(--white);font-weight:300;font-size:24px;line-height:33px;margin-top:-128px;top:194px}
.hero-text{position:absolute;top:210px;left:244px;width:372px;text-align:center;color:var(--white);font-size:8.2px;line-height:16px;font-weight:300}
.dots{position:absolute;top:335px;left:402px;display:flex;gap:3px}
.dots span{width:13px;height:4px;background:var(--white)}
.dots span.on{background:var(--purple)}
.about{position:absolute;top:440px;left:0;width:860px;height:276px}
.about h2{position:absolute;left:116px;top:30px;font-size:24px;font-weight:400;color:var(--ink)}
.about-text{position:absolute;left:116px;top:75px;width:392px}
.about-text p{font-size:8.1px;line-height:14.4px;color:var(--ink);margin-bottom:14.4px}
.about-art{position:absolute;left:522px;top:68px;width:226px;height:128px;border-radius:50%;background:
  radial-gradient(circle 28px at 50% 55%,rgba(4,85,163,.35),transparent 80%),
  radial-gradient(circle 18px at 50% 12%,rgba(107,68,155,.45),transparent 80%),
  radial-gradient(ellipse,#c9d3ee 0%,#dde3f4 55%,#f4f5fb 85%,#ffffff 100%)}
.services{position:absolute;top:717px;left:0;width:860px;height:345px;background:linear-gradient(90deg,var(--blue),var(--purple))}
.card{position:absolute;top:49px;width:197px;height:252px;background:var(--white);padding:8px}
.card-photo{height:135px}
.card h3{margin-top:12px;font-family:"Rubik",sans-serif;font-size:13.6px;font-weight:500;color:var(--purple)}
.card p{margin-top:8px;font-size:7.6px;line-height:13.4px;width:162px;color:var(--ink)}
.footer{position:absolute;top:1062px;left:0;width:860px;height:138px;background:var(--footer);color:var(--white);text-align:center}
.footer-links{position:absolute;top:38px;width:860px;font-size:8.8px}
.footer-links span{margin:0 6px}
.copyright{position:absolute;top:58px;width:860px;font-size:8.8px}
.social{position:absolute;top:84px;left:366px;display:flex;gap:3px}
.social a{width:30px;height:30px;border:1.5px solid var(--white);border-radius:50%;display:block}
</style>
</head>
<body>
<div class="topline"></div>
<header class="header">
  <div class="brand"><span class="brand-mark"></span><span class="brand-name">ROUSE</span></div>
  <nav class="nav">
    <a class="active" style="left:425px">HOME</a>
    <a style="left:490px">ABOUT</a>
    <a style="left:546px">SOLUTION</a>
    <a style="left:615px">EMPLOYMENT</a>
    <a style="left:699px">CONTACT</a>
  </nav>
</header>

<section class="hero">
  <div class="hero-photo" role="img" aria-label="Hands framing glowing hexagon healthcare icons over a doctor"></div>
  <h1 class="hero-title">It’s time to wake up<br>with Rouse Technologies.</h1>
  <p class="hero-text">Disruption isn’t just coming – it’s already here and it’s time to wake up to the new world we live in. Here at Rouse Technologies, we embrace the future that disruption brings and make it our aim to assist the world in embracing this bright future with us. We help bring businesses and people adapt to new approaches to old problems.</p>
  <div class="dots"><span></span><span></span><span class="on"></span><span></span></div>
</section>

<section class="about">
  <h2>What we do</h2>
  <div class="about-text">
    <p>We are engineers, problem-solvers, people persons, and a friendly face. We want to solve your problem in a way that won’t break the bank, give headaches, leave you with a smile on your face, and keep you smiling throughout our relationship.</p>
    <p>We predominantly work in the healthcare IT industry assisting hospitals and clinics with their IT infrastructure and information workflows. We provide software solutions and interoperability services to connect platforms and give care givers a simple view of patient records.</p>
    <p>Rouse Technologies is also exploring the world of 3D printing and how it can fully affect the healthcare industry and small businesses with Rouse3D. 3D printing is a great solution to what used to be a very niche industry.</p>
  </div>
  <div class="about-art" role="img" aria-label="Line illustration of medical icons arranged in an oval"></div>
</section>

<section class="services">
  <article class="card" style="left:116px">
    <div class="card-photo" role="img" aria-label="Vintage beige desktop computers on a desk" style="background:radial-gradient(ellipse 60px 45px at 110px 45px,#e2dac2,transparent 80%),radial-gradient(ellipse 45px 40px at 40px 65px,#d8cfb6,transparent 80%),linear-gradient(180deg,#b9b2a4 0%,#a59d8c 55%,#2f2c29 78%,#4a4640 100%)"></div>
    <h3>Computer Archeology</h3>
    <p>Need data off a legacy system that you would like to sunset? We can help you with that.</p>
  </article>
  <article class="card" style="left:331px">
    <div class="card-photo" role="img" aria-label="Doctor in a white coat using a tablet in a waiting room" style="background:radial-gradient(ellipse 40px 70px at 70px 80px,#f4f4f2,transparent 80%),radial-gradient(ellipse 70px 25px at 140px 85px,#d9a964,transparent 80%),linear-gradient(180deg,#dcdad6 0%,#c9c5bf 60%,#b2aea8 100%)"></div>
    <h3>Digital Check In</h3>
    <p>Still using clipboards to check people into your facility? Struggling to get that paper-based information into your system? We can help you with that.</p>
  </article>
  <article class="card" style="left:546px">
    <div class="card-photo" role="img" aria-label="3D printer nozzle printing a pink part" style="background:radial-gradient(ellipse 55px 35px at 90px 75px,#e3388f,transparent 85%),linear-gradient(165deg,#1e4fb4 0%,#5a8ddc 35%,#b9cff0 70%,#e8eef8 100%)"></div>
    <h3>Rouse3D</h3>
    <p>Have something in mind that you need printed, but don’t have a 3D printer? We can help you design it, and print it for you.</p>
  </article>
</section>

<footer class="footer">
  <div class="footer-links">Home <span>|</span> About <span>|</span> Solution <span>|</span> Employment <span>|</span> Contact</div>
  <div class="copyright">© 2018 Rousetech. All Rights are Reserved. Privacy Policy | Terms of Use | Site map</div>
  <div class="social"><a aria-label="Social profile one"></a><a aria-label="Social profile two"></a><a aria-label="Social profile three"></a></div>
</footer>
</body>
</html>
```